Ink Over Here needs a New Website Design

Ink Over Here is a small rubber stamp & scrapbook company operating in the arts & crafts space. We currently own 6 company brands plus Ink Over Here which is the main business & website, www.inkoverhere.net.
We are launching a new eCommerce store to bring all the companies under one shopping platform instead of the 6 there are currently. We need a new site design that incorporates the shop by brand idea making it super easy to navigate and understand. Brand logos should be displayed on all pages in header design similar to http://www.plainweave-example.com and https://bazaar.quorvix-example.com
The brand logo for Bravo! Stamps is currently being designed so that one is missing from the brief.
Top menu: Home, Shop, Videos, Gallery, Blogs, Show Schedule, IOH Brands or Brands
Utilize “Welcome to InkOverHere” tagline in design
Include “Art Rubber Stamps and Scrapbooking Supplies” tagline on at least home page
Need 3 pages designed, must be designed with responsive in mind.
Home page
Product Listing page
Product Detail page
Colors
Browns - use colors from background image attached
#981E1E
# 3B2313
Competitors
http://craftrunsfree-example.com
https://inkersunnamed-example.com
http://www.mirellsllc-example.com
http://www.tovalendesign-example.com
http://www.quaprints-example.com
http://www.juniperprints-example.us
The shopping cart system being used is Cartwell (http://demo.cartwell-example.com/) if you are familiar with creating html templates for Cartwell there is additional opportunity to convert the design into html/css
Handmade Cardmakers, Scrapbookers, Papercrafters

```html
<!DOCTYPE html>
<html lang="en">
<head>
<meta charset="utf-8">
<title>Ink Over Here – Art Rubber Stamps and Scrapbooking Supplies</title>
<link rel="stylesheet" href="https://fonts.googleapis.com/css2?family=Oswald:wght@500;600&family=Open+Sans:wght@400;600&family=Raleway:wght@700&family=Roboto+Condensed:wght@700&family=Rubik+Dirt&display=swap">
<style>
:root{
  --red:#981e1e;
  --brown:#3b2313;
  --brown-dark:#2a180c;
  --ink:#333;
  --muted:#555;
  --page:#f8f6f6;
  --paper:#ecebea;
  --line:#e4e0e0;
  --yellow:#f5d34a;
  --white:#fff;
}
*{box-sizing:border-box;margin:0;padding:0}
html,body{width:1200px;height:2222px;overflow:hidden}
body{position:relative;background:var(--page);font-family:"Open Sans",sans-serif;color:var(--ink)}
.abs{position:absolute}

/* header */
.header-band{left:0;top:0;width:1200px;height:300px;background:linear-gradient(180deg,#fff 0,#fff 80px,var(--paper) 95px,#f4f3f2 200px,var(--page) 300px)}
.site-logo{left:160px;top:30px;display:flex;align-items:center;gap:8px;width:150px}
.site-logo .dot{width:34px;height:34px;border-radius:50%;background:var(--brown);flex:none}
.site-logo .name{font-family:"Oswald",sans-serif;font-weight:600;font-size:24px;line-height:26px;color:var(--brown);text-transform:uppercase}
.brand-row{left:407px;top:18px;width:631px;height:44px;display:flex;align-items:center;justify-content:space-between}
.brand{font-family:"Open Sans",sans-serif;font-weight:600;font-size:13px;color:var(--brown);white-space:nowrap}
.brand-badge{width:78px;height:40px;background:#8fa9c4}
.util{left:600px;top:118px;width:438px;display:flex;align-items:center;justify-content:flex-end;gap:28px;font-size:11px;color:var(--ink)}
.util .lang{display:flex;align-items:center;gap:5px}
.util .flag{width:11px;height:8px;background:#c7313a}
.util .cart{display:flex;align-items:center;gap:8px;color:var(--red)}
.util .cart i{width:30px;height:30px;border-radius:50%;background:var(--red);display:flex;align-items:center;justify-content:center}

/* nav */
.main-nav{left:161px;top:170px;width:877px;height:48px;background:var(--brown);display:flex}
.main-nav a{font-family:"Roboto Condensed",sans-serif;font-weight:700;font-size:14px;color:var(--white);text-decoration:none;line-height:48px;padding:0 14px}
.main-nav a.active{background:var(--brown-dark);padding:0 22px}
.search{margin-left:auto;width:219px;height:48px;background:var(--red);display:flex;align-items:center;justify-content:space-between;padding:0 18px 0 14px}
.search span{font-size:11px;font-style:italic;color:#f1dede}

/* hero */
.hero{left:161px;top:227px;width:877px;height:457px;background:linear-gradient(120deg,#6b5a52 0,#a38a78 30%,#c9a27b 55%,#b4624a 80%,#8a6a5c 100%)}
.hero-copy{left:90px;top:65px;font-family:"Rubik Dirt",sans-serif;color:var(--white);line-height:1}
.hero-copy .l1{font-size:40px}
.hero-copy .l2{font-size:60px;margin-top:4px}
.hero-copy .l3{font-size:38px;margin-top:6px}
.hero-copy .l4{font-size:64px;margin-top:6px}
.hero-arrow{top:214px;width:34px;height:34px;border:1.5px solid rgba(255,255,255,.8);border-radius:50%;display:flex;align-items:center;justify-content:center}

/* intro */
.intro-title{left:161px;top:736px;font-family:"Oswald",sans-serif;font-weight:600;font-size:21px;color:var(--brown);letter-spacing:.5px}
.intro-text{left:161px;top:780px;width:632px;font-size:10.4px;line-height:18px;color:var(--muted)}
.intro-photo{left:819px;top:715px;width:216px;height:216px;border-radius:50%;background:radial-gradient(circle at 45% 35%,#c9d6e4,#5d6f88 55%,#2c3a52)}

/* product sections */
.section-head{left:161px;width:877px;height:32px;border-bottom:4px solid var(--brown)}
.section-head h2{font-family:"Oswald",sans-serif;font-weight:600;font-size:20px;color:var(--brown);line-height:22px;letter-spacing:.5px}
.pager{position:absolute;right:0;top:4px;display:flex;gap:2px}
.pager b{width:23px;height:22px;background:#dcdcdc;display:flex;align-items:center;justify-content:center;font-size:12px}
.grid{left:161px;width:877px;display:flex;justify-content:space-between}
.card{position:relative;width:206px;height:330px;background:var(--white);border:1px solid var(--line);text-align:center;overflow:hidden}
.card .img{width:134px;height:134px;margin:18px auto 0}
.card h3{font-family:"Raleway",sans-serif;font-weight:700;font-size:14px;margin-top:26px;color:#222}
.card p{font-size:10.5px;line-height:16px;color:var(--muted);margin:8px auto 0;width:172px}
.card .price{font-family:"Raleway",sans-serif;font-weight:700;font-size:17px;margin-top:10px;color:#222}
.buy{display:inline-flex;margin-top:12px;height:33px}
.buy i{width:26px;background:var(--brown);display:flex;align-items:center;justify-content:center}
.buy span{background:var(--red);color:var(--white);font-size:12px;font-weight:600;line-height:33px;padding:0 16px}
.ribbon{position:absolute;left:0;top:0;width:0;height:0;border-top:50px solid var(--yellow);border-right:50px solid transparent}
.ribbon em{position:absolute;left:4px;top:-40px;font-style:normal;font-size:9px;font-weight:600;color:var(--white);transform:rotate(-45deg)}

/* features */
.features{left:0;top:1826px;width:1200px;height:114px;background:var(--white)}
.feature-row{left:161px;top:1868px;width:877px;display:flex;justify-content:space-between}
.feature{display:flex;gap:10px;align-items:flex-start;width:215px}
.feature b{display:block;font-family:"Oswald",sans-serif;font-weight:500;font-size:11px;color:var(--brown);text-transform:uppercase}
.feature span{display:block;font-size:9.5px;color:var(--muted);text-transform:uppercase;margin-top:6px}

/* footer */
.footer{left:0;top:1940px;width:1200px;height:227px;background:var(--brown)}
.footer-logo{left:150px;top:2020px;display:flex;align-items:center;gap:8px;width:170px}
.footer-logo .dot{width:34px;height:34px;border-radius:50%;background:var(--white);flex:none}
.footer-logo .name{font-family:"Oswald",sans-serif;font-weight:600;font-size:24px;line-height:26px;color:var(--white);text-transform:uppercase}
.fcol{top:1990px;color:var(--white)}
.fcol h4{font-family:"Oswald",sans-serif;font-weight:600;font-size:15px;text-transform:uppercase;margin-bottom:12px}
.fcol li{list-style:none;font-size:11.5px;line-height:22px;color:#eee}
.fcol p{font-size:11.5px;color:#eee}
.email{width:246px;height:32px;background:var(--white);border-radius:2px;margin-top:12px;font-size:11px;color:#666;padding:8px 10px}
.subscribe{width:114px;height:36px;border:2px solid var(--white);margin-top:9px;font-family:"Oswald",sans-serif;font-weight:500;font-size:14px;text-align:center;line-height:32px}
.bottom-bar{left:0;top:2167px;width:1200px;height:55px;background:var(--red)}
.copyright{left:161px;top:2186px;font-size:10.5px;color:var(--white)}
.social{left:906px;top:2179px;display:flex;gap:4px}
.social i{width:30px;height:30px;border:1.5px solid var(--white);border-radius:50%}
</style>
</head>
<body>

<div class="abs header-band"></div>
<div class="abs site-logo"><span class="dot"></span><span class="name">Ink Over Here</span></div>
<div class="abs brand-row">
  <span class="brand">Brightline Impressions</span>
  <span class="brand">Crafty</span>
  <span class="brand-badge"></span>
  <span class="brand">QRT Rally</span>
  <span class="brand">L M Sparkle</span>
</div>
<div class="abs util">
  <span>Create Account</span><span>Login</span><span>$ USD</span>
  <span class="lang"><i class="flag"></i>English ▾</span>
  <span class="cart"><i><svg width="14" height="12" viewBox="0 0 14 12"><path d="M0 1h3l2 7h7l2-5H4" fill="none" stroke="#fff" stroke-width="1.6"/><circle cx="6" cy="10.5" r="1.2" fill="#fff"/><circle cx="11" cy="10.5" r="1.2" fill="#fff"/></svg></i>(0 item) - $0.00 ▾</span>
</div>

<nav class="abs main-nav">
  <a class="active">Home</a><a>Shop</a><a>Videos</a><a>Gallery</a><a>Blogs</a><a>Show Schedule</a><a>IOH Brands</a><a>Contact Us</a>
  <div class="search"><span>Enter a keyword..</span>
    <svg width="18" height="18" viewBox="0 0 18 18"><circle cx="7.5" cy="7.5" r="5.5" fill="none" stroke="#fff" stroke-width="2.4"/><path d="M11.5 11.5l5 5" stroke="#fff" stroke-width="2.6"/></svg></div>
</nav>

<section class="abs hero" role="img" aria-label="Craft table with scissors, paper flowers, buttons and a paper punch">
  <div class="abs hero-copy">
    <div class="l1">Welcome</div>
    <div class="l2">to InkOverHere</div>
    <div class="l3">Art Rubber Stamps and</div>
    <div class="l4">Scrapbooking</div>
    <div class="l4">Supplies</div>
  </div>
  <div class="abs hero-arrow" style="left:22px"><svg width="10" height="10"><path d="M7 1L3 5l4 4" fill="none" stroke="#fff" stroke-width="1.5"/></svg></div>
  <div class="abs hero-arrow" style="right:22px"><svg width="10" height="10"><path d="M3 1l4 4-4 4" fill="none" stroke="#fff" stroke-width="1.5"/></svg></div>
</section>

<h1 class="abs intro-title">SCRAPBOOKING, PAPERCRAFTING, CARD MAKING SUPPLIES.</h1>
<p class="abs intro-text">Sptas sit aspernatur aut odit aut fugit, sed quia conseq uuntur magni dolores eos qui ratione voluptatem sequi nesciunt. Neque porro quisquam est, qui dolorem ipsum qu ia dolor sit amet, consectetur, adipisci velit, sed quia non numquam eius modi tempo ra incidunt ut labore et dolore magnam aliquamptas sit aspernatur aut odit aut fugit, sed quia conseq uuntur magni dolores eos qui ratione voluptatem sequi nesciunteque porro quisquam est, qui dolorem ipsum qu ia dolor sit amet, consectetur, adipisci velit, sed quia non numquam eius modi tempo ra incidunt ut labore et dolore magnam aliquest, qui dolorem ipsum qu ia dolor sit amet, consectetur, adipisci velit, sed quia non numquam eius modi tempo ra incidunt ut labore et dolore magnam aliquam.</p>
<div class="abs intro-photo" role="img" aria-label="Shop wall displaying framed stamped cards"></div>

<!-- latest products -->
<div class="abs section-head" style="top:950px"><h2>LATEST PRODUCTS</h2><div class="pager"><b>‹</b><b>›</b></div></div>
<div class="abs grid" style="top:1013px">
  <article class="card"><div class="ribbon"><em>NEW</em></div>
    <div class="img" role="img" aria-label="Black and white winged insect stamp image" style="background:linear-gradient(135deg,#eee,#999)"></div>
    <h3>Moth Evening Coat</h3><p>Lorem ipsum dolor sit amet, conse ctetur adipiscing elit, sed do eiu</p><div class="price">$85.00</div>
    <div class="buy"><i><svg width="12" height="10" viewBox="0 0 14 12"><path d="M0 1h3l2 7h7l2-5H4" fill="none" stroke="#fff" stroke-width="1.8"/></svg></i><span>Buy Now</span></div></article>
  <article class="card">
    <div class="img" role="img" aria-label="Clear film sheet in packaging" style="background:linear-gradient(180deg,#ddd,#8a8a8a)"></div>
    <h3>ClearGlaze Sheet</h3><p>Lorem ipsum dolor sit amet, conse ctetur adipiscing elit, sed do eiu</p><div class="price">$85.00</div>
    <div class="buy"><i><svg width="12" height="10" viewBox="0 0 14 12"><path d="M0 1h3l2 7h7l2-5H4" fill="none" stroke="#fff" stroke-width="1.8"/></svg></i><span>Buy Now</span></div></article>
  <article class="card"><div class="ribbon"><em>NEW</em></div>
    <div class="img" role="img" aria-label="Vintage illustrated card" style="background:linear-gradient(160deg,#e8b49a,#b8624e)"></div>
    <h3>Moth Evening Coat</h3><p>Lorem ipsum dolor sit amet, conse ctetur adipiscing elit, sed do eiu</p><div class="price">$85.00</div>
    <div class="buy"><i><svg width="12" height="10" viewBox="0 0 14 12"><path d="M0 1h3l2 7h7l2-5H4" fill="none" stroke="#fff" stroke-width="1.8"/></svg></i><span>Buy Now</span></div></article>
  <article class="card">
    <div class="img" role="img" aria-label="Grey ink marker" style="background:linear-gradient(90deg,#fff 35%,#bbb 45%,#888 55%,#fff 65%)"></div>
    <h3>Moth Evening Coat</h3><p>Lorem ipsum dolor sit amet, conse ctetur adipiscing elit, sed do eiu</p><div class="price">$85.00</div>
    <div class="buy"><i><svg width="12" height="10" viewBox="0 0 14 12"><path d="M0 1h3l2 7h7l2-5H4" fill="none" stroke="#fff" stroke-width="1.8"/></svg></i><span>Buy Now</span></div></article>
</div>

<!-- new products -->
<div class="abs section-head" style="top:1394px"><h2>NEW PRODUCTS</h2><div class="pager"><b>‹</b><b>›</b></div></div>
<div class="abs grid" style="top:1456px">
  <article class="card">
    <div class="img" role="img" aria-label="Roll of adhesive tape in packaging" style="background:radial-gradient(circle,#ddd 30%,#8a8070 60%,#ccc 75%)"></div>
    <h3>Moth Evening Coat</h3><p>Lorem ipsum dolor sit amet, conse ctetur adipiscing elit, sed do eiu</p><div class="price">$85.00</div>
    <div class="buy"><i><svg width="12" height="10" viewBox="0 0 14 12"><path d="M0 1h3l2 7h7l2-5H4" fill="none" stroke="#fff" stroke-width="1.8"/></svg></i><span>Buy Now</span></div></article>
  <article class="card">
    <div class="img" role="img" aria-label="Vintage advertisement print" style="background:linear-gradient(170deg,#7a3a22,#c48a5a)"></div>
    <h3>Moth Evening Coat</h3><p>Lorem ipsum dolor sit amet, conse ctetur adipiscing elit, sed do eiu</p><div class="price">$85.00</div>
    <div class="buy"><i><svg width="12" height="10" viewBox="0 0 14 12"><path d="M0 1h3l2 7h7l2-5H4" fill="none" stroke="#fff" stroke-width="1.8"/></svg></i><span>Buy Now</span></div></article>
  <article class="card">
    <div class="img" role="img" aria-label="Clear stamp set in packaging" style="background:linear-gradient(180deg,#dfe6ec,#a9b7c4)"></div>
    <h3>Moth Evening Coat</h3><p>Lorem ipsum dolor sit amet, conse ctetur adipiscing elit, sed do eiu</p><div class="price">$85.00</div>
    <div class="buy"><i><svg width="12" height="10" viewBox="0 0 14 12"><path d="M0 1h3l2 7h7l2-5H4" fill="none" stroke="#fff" stroke-width="1.8"/></svg></i><span>Buy Now</span></div></article>
  <article class="card">
    <div class="img" role="img" aria-label="Vintage illustrated greeting card" style="background:linear-gradient(160deg,#f0d27a,#b98a4a)"></div>
    <h3>Moth Evening Coat</h3><p>Lorem ipsum dolor sit amet, conse ctetur adipiscing elit, sed do eiu</p><div class="price">$85.00</div>
    <div class="buy"><i><svg width="12" height="10" viewBox="0 0 14 12"><path d="M0 1h3l2 7h7l2-5H4" fill="none" stroke="#fff" stroke-width="1.8"/></svg></i><span>Buy Now</span></div></article>
</div>

<!-- features -->
<div class="abs features"></div>
<div class="abs feature-row">
  <div class="feature"><svg width="54" height="30" viewBox="0 0 54 30"><rect x="0" y="3" width="34" height="20" fill="#981e1e"/><path d="M35 9h10l7 8v6H35z" fill="#981e1e"/><circle cx="10" cy="25" r="4.5" fill="#981e1e" stroke="#fff" stroke-width="2"/><circle cx="44" cy="25" r="4.5" fill="#981e1e" stroke="#fff" stroke-width="2"/></svg>
    <div><b>Free Shipping</b><span>On orders over Rs. 400</span></div></div>
  <div class="feature"><svg width="28" height="30" viewBox="0 0 28 30"><circle cx="14" cy="10" r="7" fill="#981e1e"/><path d="M2 30c0-8 5-12 12-12s12 4 12 12z" fill="#981e1e"/><path d="M5 11a9 9 0 0118 0" fill="none" stroke="#981e1e" stroke-width="2.5"/></svg>
    <div><b>1-800-555-0147</b><span>Mon-Satur, 9am-11pm</span></div></div>
  <div class="feature"><svg width="40" height="30" viewBox="0 0 40 30"><rect x="6" y="2" width="32" height="18" fill="none" stroke="#981e1e" stroke-width="2.5"/><rect x="2" y="8" width="32" height="18" fill="#981e1e"/><circle cx="18" cy="17" r="5" fill="#fff"/></svg>
    <div><b>Replacement</b><span>Within 21 days after delivery</span></div></div>
  <div class="feature"><svg width="32" height="30" viewBox="0 0 32 30"><ellipse cx="11" cy="5" rx="10" ry="4" fill="#981e1e"/><rect x="1" y="9" width="20" height="5" fill="#981e1e"/><rect x="1" y="16" width="20" height="5" fill="#981e1e"/><circle cx="23" cy="21" r="8" fill="#981e1e" stroke="#fff" stroke-width="2"/></svg>
    <div><b>Cash on Delivery</b><span>Pay when the items are delivered</span></div></div>
</div>

<!-- footer -->
<footer>
  <div class="abs footer"></div>
  <div class="abs footer-logo"><span class="dot"></span><span class="name">Ink Over Here</span></div>
  <div class="abs fcol" style="left:347px"><h4>Company</h4><ul><li>About Us</li><li>Why Products</li><li>Order Now</li><li>Testimonials</li><li>Best Sellings</li></ul></div>
  <div class="abs fcol" style="left:481px"><h4>Products</h4><ul><li>Alandit sed nulla</li><li>In ullamcorper</li><li>Est eget tempor</li><li>Cursus neque</li><li>Consectetuer</li></ul></div>
  <div class="abs fcol" style="left:638px"><h4>Support</h4><ul><li>FAQs</li><li>Privacy Policy</li><li>Recommendations</li><li>Contact</li></ul></div>
  <div class="abs fcol" style="left:790px"><h4 style="margin-bottom:4px">Sign Up Newsletter</h4><p>Please sign up here for latest deals</p>
    <div class="email">Email address</div><div class="subscribe">SUBSCRIBE</div></div>
  <div class="abs bottom-bar"></div>
  <p class="abs copyright">Copyright © 2016 Ink Over Here, All Rights Reserved. Term of Use</p>
  <div class="abs social"><i></i><i></i><i></i><i></i></div>
</footer>

</body>
</html>
```